Accounting firm needing business card / letterhead designed
Marcus T. Elbering, CPA
marcus@fernquill.com
www.fernquill.com
482 N Harlow Ave Perrysburg, OH 43719
419-555-0172

```html
<!DOCTYPE html>
<html lang="en">
<head>
<meta charset="utf-8">
<title>Fernquill Advisors – Business Card</title>
<link href="https://fonts.googleapis.com/css2?family=Montserrat:wght@500;600;800&family=Roboto:wght@400;500&display=swap" rel="stylesheet">
<style>
  :root {
    --navy: #2a2563;
    --green: #7dc243;
    --ink: #2b2b2b;
    --paper: #ffffff;
    --backdrop: #c9cacc;
  }
  html, body {
    margin: 0;
    padding: 0;
    width: 1200px;
    height: 1200px;
    overflow: hidden;
    background: var(--backdrop);
  }
  .stage {
    position: relative;
    width: 1200px;
    height: 1200px;
  }
  .card {
    position: absolute;
    top: 215px;
    width: 440px;
    height: 770px;
    background: var(--paper);
    overflow: hidden;
    box-shadow: 0 6px 18px rgba(0,0,0,0.18);
  }
  .card--front { left: 120px; }
  .card--back  { left: 640px; }

  .wave { position: absolute; left: 0; width: 100%; display: block; }
  .wave--top { top: 0; height: 120px; }
  .wave--bottom { bottom: 0; height: 200px; }
  .wave--short { height: 140px; }
  .wave .band { fill: var(--navy); }
  .wave .swoosh { fill: none; stroke: var(--paper); stroke-width: 6; }

  .brand {
    position: absolute;
    left: 0;
    width: 100%;
    text-align: center;
    font-family: "Montserrat", sans-serif;
    font-weight: 600;
    color: var(--navy);
    letter-spacing: 1px;
    white-space: nowrap;
    margin: 0;
  }
  .card--front .brand { top: 355px; font-size: 31px; }
  .card--back .brand { top: 150px; font-size: 28px; }

  .front-url {
    position: absolute;
    top: 585px;
    left: 0;
    width: 100%;
    text-align: center;
    font-family: "Roboto", sans-serif;
    font-size: 19px;
    color: var(--ink);
  }

  .person {
    position: absolute;
    top: 330px;
    left: 55px;
    right: 40px;
  }
  .person__name {
    margin: 0;
    font-family: "Montserrat", sans-serif;
    font-weight: 800;
    font-size: 26px;
    color: var(--navy);
    letter-spacing: 0.3px;
    white-space: nowrap;
  }
  .person__title {
    margin: 2px 0 0;
    font-family: "Montserrat", sans-serif;
    font-weight: 600;
    font-size: 18px;
    letter-spacing: 4px;
    color: var(--ink);
  }
  .person__rule {
    height: 3px;
    background: var(--green);
    margin-top: 10px;
    border: 0;
  }
  .address {
    position: absolute;
    top: 440px;
    left: 55px;
    margin: 0;
    font-family: "Roboto", sans-serif;
    font-style: normal;
    font-size: 19px;
    line-height: 1.3;
    color: var(--ink);
  }
  .contacts {
    position: absolute;
    top: 530px;
    left: 50px;
    margin: 0;
    padding: 0;
    list-style: none;
    font-family: "Roboto", sans-serif;
    font-size: 20px;
    color: var(--ink);
  }
  .contacts li {
    display: flex;
    align-items: center;
    gap: 10px;
    height: 28px;
  }
  .contacts svg { width: 18px; height: 18px; fill: var(--ink); flex: none; }
</style>
</head>
<body>
<main class="stage">

  <section class="card card--front" aria-label="Card front">
    <svg class="wave wave--top" viewBox="0 0 440 120" preserveAspectRatio="none" aria-hidden="true">
      <path class="band" d="M0 0 H440 V115 C330 105 200 55 0 28 Z"/>
      <path class="swoosh" d="M0 14 C150 26 300 72 440 92"/>
    </svg>
    <p class="brand">FERNQUILL ADVISORS</p>
    <div class="front-url">www.fernquill.com</div>
    <svg class="wave wave--bottom" viewBox="0 0 440 200" preserveAspectRatio="none" aria-hidden="true">
      <path class="band" d="M0 20 C150 40 300 110 440 150 V200 H0 Z"/>
      <path class="swoosh" d="M0 62 C150 70 300 130 440 176"/>
    </svg>
  </section>

  <section class="card card--back" aria-label="Card back">
    <p class="brand">FERNQUILL ADVISORS</p>
    <div class="person">
      <h1 class="person__name">MARCUS T. ELBERING</h1>
      <p class="person__title">CPA</p>
      <hr class="person__rule">
    </div>
    <address class="address">482 N Harlow Ave Perrysburg,<br>OH 43719</address>
    <ul class="contacts">
      <li>
        <svg viewBox="0 0 24 24" aria-hidden="true"><path d="M6.6 10.8a15.1 15.1 0 0 0 6.6 6.6l2.2-2.2a1 1 0 0 1 1-.25 11.4 11.4 0 0 0 3.6.57 1 1 0 0 1 1 1V20a1 1 0 0 1-1 1A17 17 0 0 1 3 4a1 1 0 0 1 1-1h3.5a1 1 0 0 1 1 1c0 1.25.2 2.45.57 3.57a1 1 0 0 1-.25 1z"/></svg>
        419-555-0172
      </li>
      <li>
        <svg viewBox="0 0 24 24" aria-hidden="true"><path d="M2 5h20v14H2z M2 5l10 8 10-8" fill="none" stroke="#2b2b2b" stroke-width="2"/></svg>
        marcus@fernquill.com
      </li>
      <li>
        <svg viewBox="0 0 24 24" aria-hidden="true"><g fill="none" stroke="#2b2b2b" stroke-width="1.8"><circle cx="12" cy="12" r="9.5"/><ellipse cx="12" cy="12" rx="4.2" ry="9.5"/><path d="M2.5 12h19M4 7h16M4 17h16"/></g></svg>
        www.fernquill.com
      </li>
    </ul>
    <svg class="wave wave--bottom wave--short" viewBox="0 0 440 200" preserveAspectRatio="none" aria-hidden="true">
      <path class="band" d="M0 20 C150 40 300 110 440 150 V200 H0 Z"/>
      <path class="swoosh" d="M0 62 C150 70 300 130 440 176"/>
    </svg>
  </section>

</main>
</body>
</html>
```